ROVA NET LTD

Advertisement to get more schools:
use website https://www.rova-net.co.uk for logos etc.
ICT Service Level Agreements for as little as £2000 per year
Unlimited Remote, phone and email support
Unlimited Call outs included
90% fix time within 30 minutes of ticket submission
Extra support during Brelcom inspections
GDPR service included

Education

```html
<!DOCTYPE html>
<html lang="en">
<head>
<meta charset="utf-8">
<title>ROVA NET LTD – ICT Support for Schools</title>
<link rel="stylesheet" href="https://fonts.googleapis.com/css2?family=Montserrat:wght@500;600;700&family=Roboto:wght@400&display=swap">
<style>
  :root {
    --brand-blue: #0f72bd;
    --brand-orange: #f47c44;
    --ink: #222222;
    --muted: #666666;
    --paper: #ffffff;
    --hero-dark: #3b3530;
    --hero-mid: #6b6a68;
    --hero-light: #a9acae;
  }
  * { box-sizing: border-box; margin: 0; padding: 0; }
  html, body { width: 1200px; height: 2527px; overflow: hidden; background: var(--paper); }
  body { position: relative; font-family: "Roboto", sans-serif; color: var(--ink); }

  .site-header { height: 108px; display: flex; align-items: center; justify-content: center; }
  .brand { display: flex; align-items: center; gap: 14px; }
  .brand-square { width: 34px; height: 34px; background: var(--brand-blue); border-radius: 4px; }
  .brand-name { font-family: "Montserrat", sans-serif; font-weight: 700; font-size: 40px; line-height: 1; color: var(--brand-blue); letter-spacing: 1px; }

  .hero { position: absolute; top: 108px; left: 0; width: 1200px; height: 747px; background: var(--brand-blue); border-radius: 0 0 60px 60px; }
  .hero-photo { position: absolute; inset: 0 0 14px 0; border-radius: 0 0 58px 58px; overflow: hidden;
    background: linear-gradient(100deg, var(--hero-dark) 0%, #5a3a32 25%, var(--hero-mid) 55%, var(--hero-light) 100%); }
  .hero-title { position: absolute; left: 490px; top: 252px; font-family: "Montserrat", sans-serif; font-weight: 600; font-size: 63px; line-height: 83px; color: #fff; }

  .features { position: absolute; top: 982px; left: 98px; width: 1004px; display: grid; grid-template-columns: 490px 490px; column-gap: 24px; row-gap: 95px; }
  .feature-card { position: relative; height: 376px; background: var(--paper); border-radius: 8px; box-shadow: 0 4px 18px rgba(0,0,0,0.12); padding: 108px 32px 0; text-align: center; }
  .feature-icon { position: absolute; top: -62px; left: 50%; transform: translateX(-50%); width: 140px; height: 140px; border-radius: 50%; background: var(--brand-orange); display: flex; align-items: center; justify-content: center; }
  .feature-icon svg { width: 74px; height: 74px; fill: none; stroke: #1a1a1a; stroke-width: 2.4; stroke-linecap: round; stroke-linejoin: round; }
  .feature-title { font-family: "Montserrat", sans-serif; font-weight: 500; font-size: 27px; line-height: 40px; color: var(--ink); min-height: 80px; display: flex; align-items: center; justify-content: center; padding: 0 12px; }
  .feature-text { margin-top: 16px; font-size: 20.5px; line-height: 39.5px; color: var(--muted); padding: 0 2px; }

  .site-footer { position: absolute; left: 0; bottom: 0; width: 1200px; height: 142px; background: var(--brand-blue); display: flex; align-items: center; justify-content: space-between; padding: 0 92px 0 88px; color: #fff; }
  .copyright { font-size: 25px; }
  .site-footer .brand-name { color: #fff; }
  .site-footer .brand-square { background: #fff; }
</style>
</head>
<body>
  <header class="site-header">
    <div class="brand"><span class="brand-square"></span><span class="brand-name">ROVA NET</span></div>
  </header>

  <section class="hero">
    <div class="hero-photo" role="img" aria-label="Student wearing a VR headset in a classroom with classmates and laptops"></div>
    <h1 class="hero-title">Education, Support<br>and Installation of<br>All&nbsp; Technologies</h1>
  </section>

  <main class="features">
    <article class="feature-card">
      <div class="feature-icon"><svg viewBox="0 0 64 64"><circle cx="34" cy="26" r="12"/><path d="M34 19v14M38 22c-1-2-7-2-7 1s7 2 7 5-6 3-7 1"/><path d="M8 44h8v14H8zM16 46h10l8 4h8c3 0 3 4 0 4H32M16 56h20l18-10c3-2 1-5-2-4l-12 6"/><path d="M34 4v6M28 6v4M40 6v4"/></svg></div>
      <h2 class="feature-title">ICT SLA agreements for as<br>little as £2000 per year</h2>
      <p class="feature-text">Lorem ipsum dolor sit amet,adipiscing elit, sed do eiusmod tempor incididunt ut labore et dolore magna aliqua.</p>
    </article>
    <article class="feature-card">
      <div class="feature-icon"><svg viewBox="0 0 64 64"><rect x="10" y="24" width="44" height="28" rx="2"/><path d="M4 56h56M6 52h52"/><circle cx="32" cy="34" r="5"/><path d="M24 48c0-5 4-8 8-8s8 3 8 8"/><rect x="8" y="6" width="12" height="12"/><rect x="26" y="4" width="12" height="12"/><rect x="44" y="6" width="12" height="12"/></svg></div>
      <h2 class="feature-title">Unlimited Remote, phone and<br>email support</h2>
      <p class="feature-text">Lorem ipsum dolor sit amet,adipiscing elit, sed do eiusmod tempor incididunt ut labore et dolore magna aliqua.</p>
    </article>
    <article class="feature-card">
      <div class="feature-icon"><svg viewBox="0 0 64 64"><circle cx="32" cy="30" r="9"/><path d="M20 54c0-8 5-13 12-13s12 5 12 13"/><path d="M22 30c0-8 4-13 10-13s10 5 10 13"/><path d="M10 44c-4 4 2 12 8 14l4-5-5-4-3 2c-2-2-3-4-3-6z"/><rect x="42" y="4" width="18" height="12" rx="2"/><path d="M46 8h10M46 12h6"/><path d="M14 20a22 22 0 0 1 20-12M52 40a22 22 0 0 1-8 12"/></svg></div>
      <h2 class="feature-title">Unlimited Call outs<br>included</h2>
      <p class="feature-text">Lorem ipsum dolor sit amet,adipiscing elit, sed do eiusmod tempor incididunt ut labore et dolore magna aliqua.</p>
    </article>
    <article class="feature-card">
      <div class="feature-icon"><svg viewBox="0 0 64 64"><path d="M6 22h52v6a4 4 0 0 0 0 8v6H6v-6a4 4 0 0 0 0-8z"/><rect x="12" y="27" width="40" height="10"/><path d="M14 42l6 12 40-20-4-8"/></svg></div>
      <h2 class="feature-title">90% fix time within 30 minutes<br>of ticket submission</h2>
      <p class="feature-text">Lorem ipsum dolor sit amet,adipiscing elit, sed do eiusmod tempor incididunt ut labore et dolore magna aliqua.</p>
    </article>
    <article class="feature-card">
      <div class="feature-icon"><svg viewBox="0 0 64 64"><circle cx="36" cy="26" r="16"/><circle cx="36" cy="26" r="11"/><path d="M26 38L10 54l4 4 16-16"/><path d="M28 30l5-6 4 4 6-8"/><path d="M36 6v4M36 42v4M16 26h4M52 26h4"/></svg></div>
      <h2 class="feature-title">Extra support during Brelcom<br>inspections</h2>
      <p class="feature-text">Lorem ipsum dolor sit amet,adipiscing elit, sed do eiusmod tempor incididunt ut labore et dolore magna aliqua.</p>
    </article>
    <article class="feature-card">
      <div class="feature-icon"><svg viewBox="0 0 64 64"><rect x="24" y="28" width="16" height="14" rx="2"/><path d="M27 28v-4a5 5 0 0 1 10 0v4"/><circle cx="32" cy="35" r="2"/><path d="M32 4l2 4 4 1-3 3 1 4-4-2-4 2 1-4-3-3 4-1zM14 12l1.5 3 3 .5-2 2 .5 3-3-1.5-3 1.5.5-3-2-2 3-.5zM50 12l1.5 3 3 .5-2 2 .5 3-3-1.5-3 1.5.5-3-2-2 3-.5zM8 32l1.5 3 3 .5-2 2 .5 3-3-1.5-3 1.5.5-3-2-2 3-.5zM56 32l1.5 3 3 .5-2 2 .5 3-3-1.5-3 1.5.5-3-2-2 3-.5zM16 48l1.5 3 3 .5-2 2 .5 3-3-1.5-3 1.5.5-3-2-2 3-.5zM48 48l1.5 3 3 .5-2 2 .5 3-3-1.5-3 1.5.5-3-2-2 3-.5zM32 52l1.5 3 3 .5-2 2 .5 3-3-1.5-3 1.5.5-3-2-2 3-.5z"/></svg></div>
      <h2 class="feature-title">GDPR service included</h2>
      <p class="feature-text">Lorem ipsum dolor sit amet,adipiscing elit, sed do eiusmod tempor incididunt ut labore et dolore magna aliqua.</p>
    </article>
  </main>

  <footer class="site-footer">
    <p class="copyright">© 2022 All Rights Reserved</p>
    <div class="brand"><span class="brand-square"></span><span class="brand-name">ROVA NET</span></div>
  </footer>
</body>
</html>
```